Website design 5 pages + short Video + basic graphic optimization for a luxury Homestay - Resort website

I just need the website design for the main pages and optimised graphic images. The website will be mainly based on the following single-page scroll theme.

https://marshfieldthemes.com/demo/guesthouse-one-page/
FIGMA Templates https://marshfieldthemes.com/free-figma-design-files-for-hotel-and-vacation-rentals/
You can use these templates as a starting point but create something unique and luxurious.

Find all graphics files here :
1 https://www.stashcrate.net/sc/q8k517wp2ve4r7h/AAKP_Rmuvq53bx907Lqtcfw2e
2 https://www.stashcrate.net/sh/wrtmn48kdeyzqo/AAR7HunPLE93tWxM5NS2jobke?dl=0

The following is the output :
1. Create website design ( Output high-quality PSD and JPEG files )
a. Homepage ( Example https://marshfieldthemes.com/demo/countryside2/ )
b. Blog ( Example https://marshfieldthemes.com/demo/countryside2/blog-2/ )
c. Packages ….. ( Example xxxxx )
d. Room ( Example https://marshfieldthemes.com/demo/guesthouse-one-page/accommodation/kelwyn/ )
e. About us ( Example xxxxx )
f. Contact with embedded google maps ( Example https://marshfieldthemes.com/demo/hotelclassic/contact-2/ )

2. Short Video edit – 30 to 50 seconds

3. Optimise graphics for all pages and galleries ready to be used in the website ( Output high-quality JPEG files )

```html
<!DOCTYPE html>
<html lang="en">
<head>
<meta charset="utf-8">
<title>Saffron Grove — Cottages &amp; Vedic Farm</title>
<link rel="stylesheet" href="https://fonts.googleapis.com/css2?family=Courgette&family=Arimo:wght@400;700&display=swap">
<style>
:root{
  --gold:#e9b53b;
  --gold-dark:#a57f1f;
  --gold-panel:#7a5a10;
  --ink:#222222;
  --charcoal:#2b2b2b;
  --black:#0e0e0e;
  --muted:#777777;
  --light:#f2f2f2;
  --white:#ffffff;
}
*{margin:0;padding:0;box-sizing:border-box}
html,body{width:1200px;height:4291px;overflow:hidden;background:var(--white)}
body{position:relative;font-family:"Arimo",Arial,sans-serif;color:var(--ink)}
.abs{position:absolute}
.script{font-family:"Courgette",cursive;color:var(--gold)}
.brand-top{top:200px;left:0;width:1200px;text-align:center}
.brand-top .name{font-family:"Courgette",cursive;font-size:64px;color:var(--gold);line-height:1}
.brand-top .tag{margin-top:14px;font-size:15px;letter-spacing:6px;color:#f3dca3}
.site{left:195px;top:385px;width:810px;height:3828px;background:var(--white);box-shadow:0 0 18px rgba(0,0,0,.12);overflow:hidden}
.topbar{top:0;left:0;width:810px;height:23px;background:var(--ink);color:#999;font-size:7px;line-height:23px}
.topbar .login{right:0;top:0;width:23px;height:23px;background:var(--gold-dark)}
.nav{top:23px;left:0;width:810px;height:70px;background:var(--white)}
.nav a{position:absolute;top:31px;font-size:8px;color:#666;text-decoration:none;letter-spacing:.5px}
.nav a.active{color:var(--gold)}
.nav-logo{left:323px;top:23px;width:144px;height:97px;background:var(--ink);text-align:center;padding-top:34px;z-index:3}
.nav-logo .name{font-family:"Courgette",cursive;color:var(--gold);font-size:22px}
.nav-logo .tag{font-size:5px;color:var(--gold);letter-spacing:2px;margin-top:3px}
.photo{display:block}
.hero{top:93px;left:0;width:810px;height:450px;background:linear-gradient(180deg,#6fa6df 0%,#b9d6ee 22%,#5f8f3b 45%,#2f5d1f 75%,#1d3a16 100%)}
.hero-text{top:262px;left:0;width:810px;text-align:center;color:var(--white)}
.hero-text .script{font-size:19px}
.hero-text h1{font-weight:400;font-size:21px;letter-spacing:5px;margin-top:8px}
.hero-text p{font-size:9px;margin-top:8px;color:#eee}
.hero-text p span{color:var(--gold)}
.booking{top:447px;left:110px;width:588px;height:55px;background:rgba(40,40,40,.85);display:flex;align-items:center;padding:0 18px;gap:12px}
.booking .label{font-size:6px;color:var(--white);width:60px}
.booking .field{width:88px;height:22px;background:rgba(255,255,255,.12);border:1px solid rgba(255,255,255,.15);font-size:6px;color:#aaa;padding:7px 6px}
.btn{display:inline-block;background:var(--gold-dark);color:var(--white);font-size:7px;text-align:center;letter-spacing:.5px}
.booking .btn{width:66px;height:22px;line-height:22px;margin-left:8px}
.section-title{left:0;width:810px;text-align:center}
.section-title .script{font-size:16px}
.section-title h2{font-weight:400;font-size:20px;margin-top:4px;color:var(--ink)}
.section-title.dark h2{color:var(--white)}
.intro{top:658px;left:200px;width:410px;text-align:center;font-size:8px;line-height:14px;color:var(--muted)}
.room{top:728px;width:182px;height:235px}
.room .img{position:absolute;top:0;left:0;width:182px;height:195px}
.room .cap{position:absolute;left:12px;top:124px;width:158px;height:72px;background:var(--charcoal);text-align:center;padding-top:18px}
.room .cap .script{font-size:11px}
.room .cap b{display:block;font-weight:400;font-size:11px;color:var(--white);margin-top:5px}
.room .book{position:absolute;left:12px;top:196px;width:158px;height:18px;line-height:18px;background:#3a3a3a;color:#ddd;font-size:6px;text-align:center}
.room .book.gold{background:var(--gold-dark);color:var(--white)}
.packages-photo{top:1003px;left:0;width:405px;height:432px;background:linear-gradient(160deg,#32481f,#1c2914 55%,#26302a)}
.packages{top:1003px;left:405px;width:405px;height:432px;background:var(--charcoal)}
.pkg{width:150px;text-align:center}
.pkg svg{display:block;margin:0 auto}
.pkg h4{font-weight:400;font-size:7px;color:var(--gold);margin-top:6px}
.pkg p{font-size:6px;line-height:10px;color:#888;margin-top:5px}
.packages .btn{left:138px;top:370px;width:128px;height:22px;line-height:22px}
.amen{top:1522px;left:105px;width:160px}
.amen .script{font-size:14px}
.amen p{font-size:7px;line-height:12px;color:#555;margin-top:5px}
.amen ul{list-style:none;margin-top:10px}
.amen li{font-size:6px;color:#444;display:flex;align-items:center;gap:10px;height:22px}
.amen .btn{width:78px;height:20px;line-height:20px;margin-top:12px}
.amen-photo{top:1497px;left:260px;width:290px;height:246px;background:radial-gradient(ellipse at 60% 60%,#6b4514 0%,#2a1a0b 40%,#0b0b0b 80%)}
.counter{top:1518px;left:550px;width:153px;height:200px;background:var(--charcoal);text-align:center;padding-top:50px}
.counter h3{font-weight:400;font-size:13px;color:var(--white)}
.digits{display:flex;justify-content:center;gap:3px;margin-top:20px}
.digits span{width:25px;height:40px;background:#3b3b3b;border:1px solid #555;border-radius:3px;color:var(--white);font-size:26px;line-height:40px}
.gallery{top:1803px;left:0;width:810px;height:495px;background:var(--black)}
.filters{top:127px;left:0;width:810px;text-align:center;font-size:7px;color:#ccc}
.filters .on{color:var(--gold)}
.g-img{top:162px;height:250px}
.arrow{width:16px;height:16px;border:1px solid #888;color:#ccc;font-size:10px;line-height:14px;text-align:center}
.blog-card{top:2420px;width:187px}
.blog-card .img{height:158px}
.blog-card .date{font-size:6px;color:#555;margin-top:12px}
.blog-card h4{font-size:8px;margin-top:14px;color:var(--ink)}
.blog-card p{font-size:7px;line-height:12px;color:#888;margin-top:6px;text-align:justify}
.blog-card .more{font-size:6px;color:var(--gold);margin-top:8px;display:block}
.side-arrow{width:20px;height:20px;border:1px solid var(--gold);color:var(--gold);font-size:11px;line-height:18px;text-align:center;background:var(--white)}
.about-photo{top:2777px;left:0;width:330px;height:283px;background:linear-gradient(135deg,#2f4b1a,#8c8a12 45%,#3d5a1d)}
.about{top:2777px;left:330px;width:375px;height:283px;background:var(--gold-panel);padding:32px 24px}
.about .script{font-size:17px}
.about h3{font-weight:400;font-size:11px;color:#f2e2bb;margin-top:8px}
.about p{font-size:7px;line-height:13px;color:#eadcb8;margin-top:12px;text-align:justify}
.about-photo-r{top:2777px;left:705px;width:105px;height:283px;background:linear-gradient(180deg,#213a15,#5d7f33 60%,#2b4519)}
.t-card{top:3193px;width:292px;height:97px;background:var(--light);padding:18px 16px;display:flex;gap:14px}
.t-card .avatar{width:56px;height:56px;border-radius:50%;border:2px solid var(--gold);background:#c9a37a;flex:none}
.t-card h5{font-weight:400;font-size:7px}
.t-card .stars{color:var(--gold);font-size:7px;letter-spacing:1px}
.t-card p{font-size:7px;line-height:12px;color:#666;margin-top:2px}
.map{top:3348px;left:0;width:810px;height:284px;background:linear-gradient(135deg,#eef0f2,#e3e8ec 50%,#f1f3f5)}
.contact{top:3432px;left:127px;width:261px;height:158px;background:#3a3a3a;padding:26px 26px}
.contact .script{font-size:17px;margin-left:2px}
.contact .row{display:flex;gap:16px;margin-top:12px;align-items:center}
.contact .mini{font-family:"Courgette",cursive;color:var(--gold);font-size:10px;width:42px;text-align:center}
.contact p{font-size:8px;line-height:14px;color:#ddd}
.footer{top:3632px;left:0;width:810px;height:196px;background:var(--black);text-align:center}
.footer .nl{font-size:7px;color:#aaa;margin-top:44px;letter-spacing:1px}
.footer form{display:flex;justify-content:center;margin-top:8px}
.footer .input{width:150px;height:24px;border:1px solid var(--gold-dark);font-size:6px;color:#666;line-height:22px}
.footer .btn{width:80px;height:24px;line-height:24px;background:var(--gold-dark)}
.footer .copy{position:absolute;bottom:12px;width:810px;font-size:6px;color:#777}
.footer .copy span{color:var(--gold)}
</style>
</head>
<body>

<header class="abs brand-top">
  <div class="name">Saffron Grove</div>
  <div class="tag">COTTAGES &amp; VEDIC FARM</div>
</header>

<main class="abs site">
  <div class="abs topbar">
    <span class="abs" style="left:105px">Contact us : stay@saffrongrove.example</span>
    <span class="abs" style="left:233px">Call Us : +1 555 210 4418</span>
    <span class="abs" style="left:548px">Stay Connected</span>
    <span class="abs login"></span>
  </div>

  <nav class="abs nav">
    <a class="active" style="left:112px">HOME</a>
    <a style="left:185px">ROOMS</a>
    <a style="left:260px">PACKAGES</a>
    <a style="left:485px">BLOG</a>
    <a style="left:553px">ABOUT US</a>
    <a style="left:643px">CONTACT US</a>
  </nav>
  <div class="abs nav-logo">
    <div class="name">Saffron Grove</div>
    <div class="tag">COTTAGES &amp; VEDIC FARM</div>
  </div>

  <div class="abs hero photo" role="img" aria-label="Green A-frame cottage on a wooded hillside under a blue sky"></div>
  <div class="abs hero-text">
    <div class="script">Welcome to our</div>
    <h1>COTTAGE &amp; VEDIC FARM</h1>
    <p>Give yourself a <span>moment to relax</span>. Find a minute to <span>rejuvenate your body</span></p>
  </div>
  <div class="abs booking">
    <div class="label">GET IN TOUCH</div>
    <div class="field">Email</div>
    <div class="field">Name</div>
    <div class="field">Phone</div>
    <div class="field">Date</div>
    <div class="btn">SUBMIT</div>
  </div>

  <div class="abs section-title" style="top:578px">
    <div class="script">Our Room's</div>
    <h2>VEDIC ENERGIES AHEAD</h2>
  </div>
  <p class="abs intro">Simple rooms with warm wood and soft light, set among the trees so that every stay begins quietly and ends rested, calm and renewed.</p>

  <article class="abs room" style="left:105px">
    <div class="img photo" role="img" aria-label="Wooden room with two single beds" style="background:linear-gradient(160deg,#b98a3e,#d9b36a 50%,#a67432)"></div>
    <div class="cap"><div class="script">Normal Room</div><b>SPECIAL OFFERS</b></div>
    <div class="book">BOOK NOW</div>
  </article>
  <article class="abs room" style="left:313px">
    <div class="img photo" role="img" aria-label="Room with red bedding and patterned rug" style="background:linear-gradient(160deg,#c08a3a,#8a2a3a 55%,#b17a36)"></div>
    <div class="cap"><div class="script">Special Room</div><b>GIFT CARDS AVAILABLE</b></div>
    <div class="book gold">BOOK NOW</div>
  </article>
  <article class="abs room" style="left:522px">
    <div class="img photo" role="img" aria-label="Bright room with a double bed and framed art" style="background:linear-gradient(160deg,#e8dcc4,#cfae6e 55%,#e6dccb)"></div>
    <div class="cap"><div class="script">Rejuvenate Room</div><b>SPECIAL ATMOSPHERE</b></div>
    <div class="book">BOOK NOW</div>
  </article>

  <div class="abs packages-photo photo" role="img" aria-label="Guests wading in a forest river beside an inflatable raft"></div>
  <section class="abs packages">
    <div class="abs pkg" style="left:28px;top:55px">
      <svg width="22" height="22" viewBox="0 0 22 22"><circle cx="11" cy="6" r="3" fill="#a57f1f"/><rect x="3" y="12" width="16" height="4" rx="2" fill="#a57f1f"/><rect x="2" y="18" width="18" height="2" fill="#a57f1f"/></svg>
      <h4>PACKAGE ONE</h4>
      <p>Gentle massage sessions for a range of wellness goals.</p>
    </div>
    <div class="abs pkg" style="left:228px;top:55px">
      <svg width="22" height="22" viewBox="0 0 22 22"><circle cx="11" cy="6" r="3" fill="#a57f1f"/><rect x="3" y="12" width="16" height="4" rx="2" fill="#a57f1f"/><rect x="2" y="18" width="18" height="2" fill="#a57f1f"/></svg>
      <h4>PACKAGE 2</h4>
      <p>Helps restore movement and ease where the body is strained.</p>
    </div>
    <div class="abs pkg" style="left:28px;top:240px">
      <svg width="22" height="22" viewBox="0 0 22 22"><rect x="2" y="10" width="18" height="6" fill="#a57f1f"/><rect x="2" y="6" width="4" height="4" fill="#a57f1f"/><rect x="3" y="16" width="2" height="4" fill="#a57f1f"/><rect x="17" y="16" width="2" height="4" fill="#a57f1f"/></svg>
      <h4>PACKAGE THREE</h4>
      <p>Warm stones placed on the body to release tension.</p>
    </div>
    <div class="abs pkg" style="left:228px;top:240px">
      <svg width="22" height="22" viewBox="0 0 22 22"><rect x="8" y="6" width="7" height="14" rx="2" fill="#a57f1f"/><path d="M14 8 L20 2" stroke="#a57f1f" stroke-width="2"/></svg>
      <h4>PACKAGE FOUR</h4>
      <p>Supports recovery and care for active bodies.</p>
    </div>
    <div class="abs btn">BOOK NOW !</div>
  </section>

  <div class="abs amen">
    <div class="script">Amenities &amp; benefits</div>
    <p>Surrounded by nature, stunning views of the countryside.</p>
    <ul>
      <li><svg width="9" height="9" viewBox="0 0 10 10"><path d="M1 5 L5 1 L9 5 V9 H1Z" fill="#222"/></svg>ENTIRE HOME</li>
      <li><svg width="9" height="9" viewBox="0 0 10 10"><path d="M1 5 L4 8 L9 2" stroke="#222" stroke-width="1.6" fill="none"/></svg>ENHANCED CLEAN</li>
      <li><svg width="9" height="9" viewBox="0 0 10 10"><circle cx="3" cy="3" r="2.2" fill="none" stroke="#222" stroke-width="1.4"/><path d="M4.5 4.5 L9 9" stroke="#222" stroke-width="1.4"/></svg>SELF CHECK-IN</li>
    </ul>
    <div class="btn">BOOK NOW !</div>
  </div>
  <div class="abs amen-photo photo" role="img" aria-label="Wooden cottage lit warmly at night"></div>
  <div class="abs counter">
    <h3>VISITORS COUNTER</h3>
    <div class="digits"><span>7</span><span>9</span><span>9</span><span>9</span><span>0</span></div>
  </div>

  <section class="abs gallery">
    <div class="abs section-title dark" style="top:44px">
      <div class="script">Our Special</div>
      <h2>GALLERY</h2>
    </div>
    <div class="abs filters"><span class="on">All Photo</span> &nbsp;|&nbsp; Garden &nbsp;|&nbsp; Room &nbsp;|&nbsp; Garden Flower &nbsp;|&nbsp; Nature &nbsp;|&nbsp; Natural Pool &nbsp;|&nbsp; Lorem Massage</div>
    <div class="abs g-img photo" role="img" aria-label="Bamboo grove beside a garden path" style="left:105px;width:183px;background:linear-gradient(160deg,#1b2a18,#5c7c2b 50%,#2a3320)"></div>
    <div class="abs g-img photo" role="img" aria-label="White flower in a green garden" style="left:293px;width:184px;background:radial-gradient(circle at 50% 45%,#e8e8e0 0%,#9aa43a 30%,#1e3418 75%)"></div>
    <div class="abs g-img photo" role="img" aria-label="Green-roofed cottage under a bright sky" style="left:483px;width:185px;background:linear-gradient(180deg,#2e6b8a,#1f5246 45%,#13281e)"></div>
    <div class="abs arrow" style="left:388px;top:432px">&lsaquo;</div>
    <div class="abs arrow" style="left:408px;top:432px">&rsaquo;</div>
  </section>

  <div class="abs section-title" style="top:2333px">
    <div class="script">Blog's</div>
    <h2>VEDIC KNOWLEDGE</h2>
  </div>
  <div class="abs side-arrow" style="left:62px;top:2492px">&lsaquo;</div>
  <div class="abs side-arrow" style="left:728px;top:2492px">&rsaquo;</div>
  <article class="abs blog-card" style="left:105px">
    <div class="img photo" role="img" aria-label="Cottage among green trees and yellow flowers" style="background:linear-gradient(180deg,#2a6fc0,#3f7d2a 45%,#b9b020)"></div>
    <div class="date">January 1, 2022</div>
    <h4>OUR ESSENTIAL VACATION TIPS</h4>
    <p>Plan light, arrive early and leave room for slow mornings. Our hosts share simple ways to settle in, walk the trails and enjoy the farm at an easy pace during your stay with us here.</p>
    <span class="more">Read more &rarr;</span>
  </article>
  <article class="abs blog-card" style="left:312px">
    <div class="img photo" role="img" aria-label="Cup of herbal drink on a table with hills behind" style="background:linear-gradient(180deg,#8fb2c7,#d8d6cf 50%,#5f8a3a)"></div>
    <div class="date">August 1, 2022</div>
    <h4>SPECIAL VEDIC DRINK</h4>
    <p>A warm blend of herbs and spices brewed each morning from the garden. Learn how we prepare it, why guests love it and how to make a simple version at home after you leave.</p>
    <span class="more">Read more &rarr;</span>
  </article>
  <article class="abs blog-card" style="left:518px">
    <div class="img photo" role="img" aria-label="White blossom in the farm garden" style="background:radial-gradient(circle at 45% 40%,#f0f0ea 0%,#7b8a3a 35%,#27401c 80%)"></div>
    <div class="date">September 20, 2022</div>
    <h4>OUR VEDIC GARDEN</h4>
    <p>Walk through the beds of herbs, flowers and vegetables that feed our kitchen. Each plant is grown by hand with care, following old seasonal rhythms and simple natural methods.</p>
    <span class="more">Read more &rarr;</span>
  </article>

  <div class="abs about-photo photo" role="img" aria-label="Yellow leaves in front of terraced green hills"></div>
  <section class="abs about">
    <div class="script">About us</div>
    <h3>WE ARE MORE THAN COTTAGE AND VEDIC FARM</h3>
    <p>Saffron Grove began as a small family farm in the hills and grew into a quiet retreat for travellers who want rest, fresh food and open air. Our cottages are built from local timber, our meals come from the garden, and our days follow the sun. Guests join morning walks, learn about herbs, share stories by the fire and leave feeling lighter. We keep the place simple, clean and warm, and we welcome every visitor as part of the family.</p>
  </section>
  <div class="abs about-photo-r photo" role="img" aria-label="Terraced fields on a green hillside"></div>

  <div class="abs section-title" style="top:3090px">
    <div class="script">Testimonials</div>
    <h2>OUR GUEST FEEDBACK</h2>
  </div>
  <div class="abs side-arrow" style="left:62px;top:3230px">&lsaquo;</div>
  <div class="abs side-arrow" style="left:728px;top:3230px">&rsaquo;</div>
  <div class="abs t-card" style="left:105px">
    <div class="avatar" role="img" aria-label="Guest portrait"></div>
    <div><h5>ELENA MARSH</h5><div class="stars">&#9733;&#9733;&#9733;&#9733;&#9733;</div><p>A peaceful stay with kind hosts and lovely food. The views from our cottage were calm and beautiful every morning.</p></div>
  </div>
  <div class="abs t-card" style="left:412px">
    <div class="avatar" role="img" aria-label="Guest portrait" style="background:#a8745a"></div>
    <div><h5>PRIYA KAUL</h5><div class="stars">&#9733;&#9733;&#9733;&#9733;&#9733;</div><p>The massage package was wonderful and the garden walks were a joy. We already plan to return next year.</p></div>
  </div>

  <div class="abs map photo" role="img" aria-label="Street map showing the retreat location with a red pin"></div>
  <div class="abs contact">
    <div class="script">Contact us</div>
    <div class="row">
      <div class="mini">Saffron Grove</div>
      <p>42 Cedar Ridge Lane, Hillview 40217<br>Email : stay@saffrongrove.example<br>Telephone : +1 (555) 210-4419</p>
    </div>
  </div>

  <footer class="abs footer">
    <div class="nl">NEWSLETTER</div>
    <form><div class="input">Enter your email address</div><div class="btn">SUBSCRIBE</div></form>
    <div class="copy">Saffron Grove &copy; 2022 All Rights Reserved <span>Terms of Use</span> and <span>Privacy Policy</span></div>
  </footer>
</main>

</body>
</html>
```